81M business card

I need a business card for a life sciences consulting firm I started. The company name is 81M and the logo is attached. I am looking for something edgey and current but different from the blah standard business card.

Industry/Entity Type

Business

Requirements
Nice to have
• Both sides

```html
<!DOCTYPE html>
<html lang="en">
<head>
<meta charset="utf-8">
<title>81M Business Card</title>
<link rel="stylesheet" href="https://fonts.googleapis.com/css2?family=Open+Sans:ital,wght@0,400;0,600;0,700;1,600&display=swap">
<style>
  :root {
    --stage: #1c1d1f;
    --stage-edge: #121314;
    --card-light: #eceeef;
    --card-light-2: #f7f8f8;
    --card-dark: #0b0b0b;
    --brand-blue: #1236d4;
    --brand-orange: #f25a12;
    --ink: #1a1f3a;
    --ink-soft: #3b3f4a;
    --muted: #6f7480;
  }
  * { margin: 0; padding: 0; box-sizing: border-box; }
  html, body {
    width: 1200px;
    height: 1200px;
    overflow: hidden;
  }
  body {
    background: radial-gradient(ellipse at 50% 40%, var(--stage) 0%, var(--stage-edge) 100%);
    font-family: "Open Sans", Arial, sans-serif;
    display: flex;
    flex-direction: column;
    align-items: center;
    justify-content: center;
    gap: 60px;
  }
  .card {
    width: 860px;
    height: 494px;
    position: relative;
    overflow: hidden;
    box-shadow: 0 14px 36px rgba(0,0,0,0.55);
  }

  /* Back side */
  .card--back {
    background: var(--card-dark);
    display: flex;
    align-items: center;
    justify-content: center;
  }
  .card--back .brand-mark {
    color: #ffffff;
    font-weight: 700;
    font-size: 170px;
    letter-spacing: 4px;
    line-height: 1;
  }

  /* Front side */
  .card--front {
    background: linear-gradient(135deg, var(--card-light-2) 0%, var(--card-light) 60%, #e3e6e8 100%);
  }
  .watermark {
    position: absolute;
    right: 40px;
    top: 120px;
    font-weight: 700;
    font-size: 230px;
    line-height: 1;
    color: rgba(120,128,140,0.08);
  }
  .holder {
    position: absolute;
    left: 40px;
    top: 78px;
  }
  .holder__name {
    font-size: 54px;
    line-height: 1;
    color: var(--ink-soft);
    font-weight: 400;
  }
  .holder__first {
    color: var(--brand-blue);
    font-weight: 700;
  }
  .holder__role {
    font-size: 20px;
    font-weight: 600;
    color: var(--ink);
    margin-top: 4px;
  }
  .address {
    position: absolute;
    left: 525px;
    top: 142px;
    font-style: italic;
    font-weight: 600;
    font-size: 22px;
    line-height: 1.35;
    color: var(--ink);
  }
  .company {
    position: absolute;
    left: 36px;
    bottom: 56px;
  }
  .company__row {
    display: flex;
    align-items: center;
    gap: 14px;
  }
  .company__dot {
    width: 58px;
    height: 58px;
    border-radius: 50%;
    background: var(--brand-orange);
  }
  .company__name {
    font-size: 64px;
    font-weight: 700;
    line-height: 1;
    color: var(--brand-blue);
  }
  .company__tagline {
    font-size: 13px;
    color: var(--muted);
    margin-top: 6px;
    margin-left: 72px;
  }
  .contact {
    position: absolute;
    left: 525px;
    top: 368px;
    font-size: 21px;
    font-weight: 600;
    line-height: 1.3;
    color: var(--ink);
    list-style: none;
  }
  .contact__label {
    display: inline-block;
    width: 40px;
    font-weight: 700;
  }
</style>
</head>
<body>
  <section class="card card--back" aria-label="Card back">
    <span class="brand-mark">81M</span>
  </section>

  <section class="card card--front" aria-label="Card front">
    <span class="watermark" aria-hidden="true">81M</span>

    <div class="holder">
      <p class="holder__name"><span class="holder__first">John</span> Doe</p>
      <p class="holder__role">manager</p>
    </div>

    <address class="address">
      Mara Lindell&nbsp; 118 Orchard Ln<br>
      Riverton,&nbsp; NY(New York)
    </address>

    <div class="company">
      <div class="company__row">
        <span class="company__dot" aria-hidden="true"></span>
        <span class="company__name">81M</span>
      </div>
      <p class="company__tagline">regulatory consulting and contract services</p>
    </div>

    <ul class="contact">
      <li><span class="contact__label">P :</span>1800 555 014</li>
      <li><span class="contact__label">M:</span>0400 555 872</li>
      <li><span class="contact__label">E :</span>admin@81m.example</li>
    </ul>
  </section>
</body>
</html>
```